Web Design for couples website

About us:
Duoperks.sg is a new startup website that aims to suggest and promote activities for young couples. The site will feature a blog and a group deals page (i.e Flockbuy).

What we need:
We require a talented designer to design a theme for the website. The design must include at least the following:
1. Logo Design - A logo should be provided along with the website design. The design should match the overall design of the website (or vice versa). The logo should include the words "Duoperks.sg" or "Duoperks". Capitalisation of the alphabets are not critical.

2 - Home / Landing page
The layout of this page should be similar to the standard 2 / 3 column wordpress pages with an image slider on top to feature articles / deals. There should also be a column on the side to include widgets such as social networking and mailing list subscription, etc

3. Deals Listing Page
This page will have a listing of all current group deals, similar to that of Flockbuy. The layout can either have deals listed in 1 or 2 columns.

4. Past Deals Page - See references below

5. Deal Page
Detailed information page for each specific deal. This should include deal image, title, buy button, timer, social media buttons, two column text.

References for deal pages:
www.bargainvale.com.sg
http://www.everyoffernest.com.au/daily-deals
www.totalsavepacific.com
www.hugeswapzo.com

6. General page design for miscellaneous pages like "About", "Contact", etc.

The overall theme of the website should cater to an audience of 18-30 year old young adults. Preferably to have something less colourful and give the overall feel of class. This should cater generally to females but males as well, so less (or no)pink / red would be preferable. But don't let yourself get restricted by these requirements and feel free to let your creative juices flow!
Updates

Hi Designers,

Thank you for your submissions so far. I would like to point out that the deal listing page will only be a sub section of the page.  Would appreciate if priority was given to the main / landing page slider and 2 or 3 columns for articles below.

Other priority would be for the single deal design, where I'm more interested to have more unique buttons such as "buy now" and "time left" .

Also to note, only .PSD design file is required. No coding (HTML / CSS) is necessary and should also be friendly for developers to work with.

Hi Designers,

 
Please submit proposal designs based on requirements on landing page or deal listings page as these would be my main requirements for consideration.

Also, Do try to keep the theme clean and easy on the eyes. Overall, I'm looking for something that is simplistic and/or classy with elegance.

Target Market(s)

18 - 30 years old young adults interested in dating and activities for couples

Industry/Entity Type

Media

Requirements
Must have
• - Logo
- Home
- Deal Page (specific)
- General layout

```html
<!DOCTYPE html>
<html lang="en">
<head>
<meta charset="utf-8">
<title>Duoperks.sg – Home</title>
<link href="https://fonts.googleapis.com/css2?family=PT+Sans:wght@400;700&family=Roboto+Condensed:wght@400;700&family=Open+Sans:wght@400;600&display=swap" rel="stylesheet">
<style>
:root{
  --sky:#bfe6fb;
  --sky-deep:#1aa7ec;
  --pink:#d6368f;
  --pink-frame:#e06aa8;
  --red:#c8101c;
  --orange:#f39a1c;
  --orange-light:#f7b84a;
  --green:#8cc222;
  --panel-blue:#3fb1ea;
  --text:#4a4a4a;
  --muted:#6b6b6b;
  --line:#d5d5d5;
  --white:#ffffff;
  --link-blue:#1b9ad8;
}
*{box-sizing:border-box;margin:0;padding:0}
html,body{width:1007px;height:1200px;overflow:hidden;background:var(--white)}
body{font-family:"Open Sans",Verdana,sans-serif;color:var(--text)}
.page{position:relative;width:1007px;height:1200px;overflow:hidden;
  background:linear-gradient(#fff 0,#fff 80px,#ececec 158px,#bfe6fb 158px,#8fd2f6 300px,#1fa8ec 432px,#f2f2f2 432px,#fff 500px,#fff 100%)}
.topbar{position:absolute;left:0;top:0;width:100%;height:13px;background:linear-gradient(#a8dcf8,#d2eefc)}
.topbar::after{content:"";position:absolute;left:0;bottom:0;width:100%;height:3px;background:#8ccff4}
.abs{position:absolute}
.brand{display:flex;align-items:center;gap:8px;font-family:"Open Sans",sans-serif;font-weight:600;color:var(--text);line-height:1;white-space:nowrap}
.brand-mark{width:14px;height:14px;border-radius:50%;background:var(--pink);flex:none}
.brand-header{position:absolute;left:102px;top:34px;font-size:30px}
.callout{left:655px;top:29px;width:248px;text-align:right;font-family:"Roboto Condensed",sans-serif;font-size:21px;color:var(--red)}
.nav{position:absolute;left:101px;top:114px;width:805px;height:34px;border-radius:4px;
  background:linear-gradient(#f7b54c,#f08a14);display:flex;overflow:hidden}
.nav a{display:flex;align-items:center;justify-content:center;height:100%;color:#fff;text-decoration:none;
  font-family:"Roboto Condensed",sans-serif;font-size:11.5px;text-transform:uppercase;border-right:1px solid #f6c57b}
.nav .current{background:linear-gradient(#a9d63b,#7cb81a);color:#2b3a05}
.search{position:absolute;right:6px;top:6px;width:126px;height:21px;background:linear-gradient(#fff,#e9e9e9);border-radius:5px;border:1px solid #e0e0e0}
.search svg{position:absolute;right:5px;top:3px}
.slider{left:101px;top:165px;width:805px;height:245px;background:var(--pink-frame);border-radius:2px}
.hero{left:107px;top:171px;width:544px;height:234px;background:linear-gradient(160deg,#c9d4df 0%,#8c9aa8 45%,#3c3a3c 100%)}
.hero-caption{left:107px;top:326px;width:544px;height:79px;background:rgba(60,60,60,.55);color:#fff;padding:6px 5px}
.hero-caption h2{font-family:"Open Sans",sans-serif;font-weight:400;font-size:18px;letter-spacing:.3px}
.hero-caption p{font-size:9.6px;line-height:13px;margin-top:8px}
.teasers{left:663px;top:173px;width:237px}
.teaser{height:56px;margin-bottom:2.5px;display:flex;align-items:center;padding:0 8px;background:var(--panel-blue)}
.teaser.active{background:linear-gradient(#f9a842,#f07a10)}
.thumb{width:84px;height:42px;border:2px solid #fff;flex:none;background:linear-gradient(135deg,#9eb6c7,#5a6a76)}
.teaser p{color:#fff;font-size:10px;line-height:13.5px;margin-left:9px}
.welcome{left:102px;top:446px;font-size:13px;color:var(--muted);display:flex;align-items:center;gap:8px}
.welcome .brand{font-size:24px}
.welcome .brand-mark{width:11px;height:11px}
.headline{position:absolute;left:102px;font-family:"Roboto Condensed",sans-serif;font-size:21px;color:var(--red);font-weight:400}
.copy{position:absolute;font-size:9.4px;line-height:12.9px;color:var(--text);text-align:justify;overflow:hidden}
.divider{position:absolute;left:101px;width:589px;height:20px;border-top:1px solid var(--line);
  background:radial-gradient(ellipse at 50% 0,rgba(0,0,0,.08),transparent 70%)}
.btn{position:absolute;height:24px;border-radius:2px;background:linear-gradient(#ffd04a,#f39a10);border:1px solid #e69314;
  color:#fff;font-size:10px;display:flex;align-items:center;text-transform:uppercase;letter-spacing:.3px}
.btn span{flex:1;text-align:center}
.btn i{width:18px;height:100%;border-left:1px solid #fbd58a;display:flex;align-items:center;justify-content:center}
.agent{left:710px;top:440px;width:160px;height:139px;background:radial-gradient(ellipse at 55% 40%,#e7d9cf,#f7f7f7 70%)}
.side-title{position:absolute;font-family:"PT Sans",sans-serif;font-weight:400;font-size:27px;color:var(--orange);text-shadow:1px 1px 1px rgba(0,0,0,.15)}
.field{position:absolute;left:703px;width:203px;height:18px;display:flex;align-items:center}
.field label{font-size:9px;color:#555;width:81px;letter-spacing:.3px}
.field b{flex:1;height:17px;background:linear-gradient(90deg,#e6e6e6,#fafafa 50%,#e2e2e2)}
.footer{left:0;top:1064px;width:1007px;height:136px;background:linear-gradient(#2aaeed,#8fd3f7 70%,#c7e9fb)}
.flinks{position:absolute;font-size:11px;color:#fff;line-height:25px}
.social{position:absolute;top:1076px;width:24px;height:24px;border-radius:4px}
.frule{left:101px;top:1156px;width:805px;height:1px;background:#2aa6e4}
.fnav{left:0;top:1162px;width:1007px;text-align:center;font-size:11px;color:var(--link-blue)}
.copyr{left:0;top:1183px;width:1007px;text-align:center;font-size:9.5px;color:var(--link-blue);letter-spacing:.3px}
</style>
</head>
<body>
<div class="page">
  <div class="topbar"></div>
  <div class="brand brand-header"><span class="brand-mark"></span>Duoperks.sg</div>
  <div class="abs callout">Call us Now! 000-000-0000</div>

  <nav class="nav">
    <a style="width:90px">Home</a>
    <a class="current" style="width:175px">Deals Page Listings</a>
    <a style="width:166px">Deal Page Specific</a>
    <a style="width:113px">About Us</a>
    <a style="width:122px">Contact Us</a>
    <div class="search">
      <svg width="15" height="14" viewBox="0 0 15 14"><circle cx="6" cy="6" r="4.3" fill="none" stroke="#8a8a8a" stroke-width="1.6"/><line x1="9.2" y1="9.2" x2="13.5" y2="13" stroke="#777" stroke-width="2.2"/></svg>
    </div>
  </nav>

  <div class="abs slider"></div>
  <div class="abs hero" role="img" aria-label="Photo of a group of young friends jumping joyfully against the sky"></div>
  <div class="abs hero-caption">
    <h2>Punch Line Goes to here</h2>
    <p>Sample text here sample Sample text here sample Sample text here sample Sample text here sample<br>Sample text here sample Sample text here sample Sample text here sample Sample text here sample</p>
  </div>
  <div class="abs teasers">
    <div class="teaser active"><div class="thumb" role="img" aria-label="Thumbnail of friends jumping"></div><p>Sample text here sample<br>Sample text here sample<br>Sample text here sample</p></div>
    <div class="teaser"><div class="thumb" role="img" aria-label="Thumbnail of a child playing"></div><p>Sample text here sample<br>Sample text here sample<br>Sample text here sample</p></div>
    <div class="teaser"><div class="thumb" role="img" aria-label="Thumbnail of children reading"></div><p>Sample text here sample<br>Sample text here sample<br>Sample text here sample</p></div>
    <div class="teaser"><div class="thumb" role="img" aria-label="Thumbnail of two girls smiling"></div><p>Sample text here sample<br>Sample text here sample<br>Sample text here sample</p></div>
  </div>

  <div class="abs welcome">Welcome to <span class="brand"><span class="brand-mark"></span>Duoperks.sg</span></div>
  <h1 class="headline" style="top:487px">Punch line goes ho hre Punch line goes ho hre</h1>
  <p class="copy" style="left:102px;top:522px;width:590px;height:117px">sample text here sample text here sample text here sample text here sample text here sample text here sample text here sample text here sample text here sample text here sample text here sample text here sample text here sample text here sample text here sample text here sample text here sample text here sample text here sample text here sample text here sample text here sample text here sample text here sample text here sample text here sample text here sample text here sample text here sample text here sample text here sample text here sample text here sample text here sample text here sample text here sample text here sample text here sample text here sample text here sample text here sample text here sample text here sample text here sample text here sample text here sample text here sample text here sample text here sample text here sample text here sample text here sample text here sample text here sample text here sample text here sample text here sample text here sample text here sample text here sample text here sample text here sample text here sample text here sample text here sample text here sample text here sample text here sample text here sample text here sample text here sample text here sample text here sample text here sample text here sample text here sample text here sample text here sample text here sample text here sample text here sample text here sample text here</p>
  <div class="divider" style="top:656px"></div>

  <h2 class="headline" style="top:691px">Punch Line Goes to Here</h2>
  <p class="copy" style="left:102px;top:728px;width:566px;height:39px">sample text here sample text here sample text here sample text here sample text here sample text here sample text here sample text sample text here sample text here sample text here sample text here sample text here sample text here sample text here sample text sample text here sample text here sample text here sample text here sample text here sample text here sample text here sample text</p>
  <div class="btn" style="left:605px;top:778px;width:84px"><span>View More</span><i><svg width="6" height="8"><path d="M1 1l3.5 3L1 7" stroke="#fff" stroke-width="1.6" fill="none"/></svg></i></div>
  <div class="divider" style="top:814px"></div>

  <h2 class="headline" style="top:861px">Punch Line Goes to Here</h2>
  <p class="copy" style="left:108px;top:905px;width:566px;height:39px">sample text here sample text here sample text here sample text here sample text here sample text here sample text here sample text sample text here sample text here sample text here sample text here sample text here sample text here sample text here sample text sample text here sample text here sample text here sample text here sample text here sample text here sample text here sample text</p>
  <div class="btn" style="left:605px;top:956px;width:84px"><span>View More</span><i><svg width="6" height="8"><path d="M1 1l3.5 3L1 7" stroke="#fff" stroke-width="1.6" fill="none"/></svg></i></div>
  <div class="divider" style="top:992px"></div>

  <div class="abs agent" role="img" aria-label="Photo of a smiling customer support agent with a headset"></div>
  <h3 class="side-title" style="left:726px;top:570px">Quick Contact</h3>
  <div class="field" style="top:624px"><label>First Name:</label><b></b></div>
  <div class="field" style="top:654px"><label>Last Name:</label><b></b></div>
  <div class="field" style="top:684px"><label>Company Name:</label><b></b></div>
  <div class="field" style="top:713px"><label>Email:</label><b></b></div>
  <div class="field" style="top:743px"><label>Phone:</label><b></b></div>
  <div class="btn" style="left:822px;top:775px;width:84px"><span>Submit</span><i><svg width="6" height="8"><path d="M1 1l3.5 3L1 7" stroke="#fff" stroke-width="1.6" fill="none"/></svg></i></div>
  <h3 class="side-title" style="left:726px;top:814px">Newsletter</h3>
  <div class="field" style="top:864px"><label>Email:</label><b></b></div>
  <div class="btn" style="left:822px;top:896px;width:84px"><span>Signup</span><i><svg width="6" height="8"><path d="M1 1l3.5 3L1 7" stroke="#fff" stroke-width="1.6" fill="none"/></svg></i></div>

  <footer class="abs footer"></footer>
  <div class="flinks" style="left:101px;top:1069px">Reference Link<br>Reference Link<br>Reference Link</div>
  <div class="flinks" style="left:236px;top:1069px">Reference Link<br>Reference Link<br>Reference Link</div>
  <div class="flinks" style="left:367px;top:1069px">Reference Link<br>Reference Link<br>Reference Link</div>
  <div class="flinks" style="left:495px;top:1069px">Reference Link<br>Reference Link<br>Reference Link</div>
  <div class="flinks" style="left:623px;top:1069px">Reference Link<br>Reference Link<br>Reference Link</div>
  <div class="social" style="left:795px;background:#3b5a9a"></div>
  <div class="social" style="left:831px;background:#4fc0ea"></div>
  <div class="social" style="left:865px;background:#1b6ca8"></div>
  <div class="abs frule"></div>
  <div class="abs fnav">Home | Deals Page Listings | Deal Page Specific | About Us | Contact Us</div>
  <div class="abs copyr">© copyright 2012 by Duoperks.sg all rights reserved.</div>
</div>
</body>
</html>
```